Volbex (Pathways for trade momentum) website

My plan is to offer a marketplace where by businesses (SME and Corporates) are able to post specific requirements, be that debt funding advice or other types of advice (legal/accountant) on the volbex website and advisors can seek to 'pitch' to the client.

clients should be anonymous - maybe a specific client number? (this is reduces the risk of bypass) and have the ability to choose the advisor via the advisors profile.

Advisors could potential use there Peerlane profile to auto complete on Volbex - not sure if this is possible or costs involved, however this would be ideal.

I would think Wordpress would be the best platform for this type of platform, however I would be guided by the experts.

I would need any code written in html 5 to allow for various devices (mobile, tablets, desktop)

Logo design is currently being completed also via Sketch Hive and I'm finalising colours ext now, so could provide advice in due course.

additional requirements (medium to longer term)
longer term I would be looking to add addition aspects to the site including algorithms, specific financial calculations, some of which I would be able to complete myself.

similar websites would be:
https://www.taskmorn.com.au
http://www.fundvale.com.au

Industry/Entity Type

Debt

Coding

Coded - Design and coding required

```html
<!DOCTYPE html>
<html lang="en">
<head>
<meta charset="utf-8">
<title>Volbex — Pathways for trade momentum</title>
<link rel="stylesheet" href="https://fonts.googleapis.com/css2?family=Arimo:ital,wght@0,400;0,700;1,400&display=swap">
<style>
:root{
  --brand:#4f63a5;
  --brand-soft:#6680bb;
  --sky:#86b9e3;
  --ink:#333a44;
  --navy:#2b4a6b;
  --muted:#7a7f87;
  --red:#e24b4b;
  --cta:#e85a5c;
  --panel:#f2f2f2;
  --band:#f5f5f5;
  --line:#e4e4e4;
  --beige:#d8c9a7;
  --teal:#2c5467;
  --footer:#333333;
  --white:#ffffff;
}
*{box-sizing:border-box;margin:0;padding:0}
html,body{width:1200px;height:3005px;overflow:hidden}
body{font-family:"Arimo",Arial,sans-serif;color:var(--ink);background:var(--white);position:relative}
.abs{position:absolute}
.center{text-align:center;left:0;width:1200px}

/* header */
.site-header{position:absolute;top:0;left:0;width:1200px;height:100px;background:var(--white)}
.brand-mark{left:132px;top:20px;width:60px;height:60px;border-radius:50%;background:var(--brand)}
.brand-name{left:206px;top:30px;font-size:34px;color:var(--brand);letter-spacing:1px}
.brand-tag{left:208px;top:66px;font-size:10px;color:var(--sky)}
.nav a{position:absolute;top:42px;height:34px;line-height:34px;font-size:14px;color:var(--ink);text-decoration:none}
.nav .active{border:2px solid var(--brand);padding:0 16px;line-height:30px;color:var(--brand)}
.btn-register{left:876px;top:32px;width:192px;height:44px;line-height:44px;text-align:center;background:var(--brand);color:var(--white);font-size:14px}

/* hero */
.hero{top:100px;left:0;width:1200px;height:502px;background:linear-gradient(180deg,#4b4a4e 0%,#8a7a73 22%,#3c4350 45%,#1f252f 100%)}
.hero-title{top:256px;font-size:34px;font-weight:700;color:var(--white);letter-spacing:1px}
.hero-sub{top:300px;font-size:26px;font-weight:700;color:var(--sky);letter-spacing:1px}
.hero-text{top:362px;font-size:15px;line-height:25px;color:var(--white)}
.dots{display:flex;gap:6px;justify-content:center}
.dots span{width:12px;height:12px;border-radius:50%;border:2px solid var(--white)}
.dots span.on{background:var(--sky);border-color:var(--sky)}

/* how */
h2{font-weight:400;font-size:30px;color:var(--ink)}
h2 b{font-weight:400;color:var(--brand)}
.step{top:744px;width:300px;height:140px;background:var(--panel)}
.step-num{position:absolute;left:0;top:0;width:80px;height:140px;background:linear-gradient(90deg,#f6f6f6,#e9e9e9);clip-path:polygon(0 0,100% 0,100% 100%,0 100%);font-size:30px;color:var(--red);padding:20px 0 0 22px}
.step-num::after{content:"";position:absolute;right:-20px;top:0;border-top:70px solid transparent;border-bottom:70px solid transparent;border-left:20px solid #e9e9e9}
.step h3{position:absolute;left:104px;top:18px;width:180px;font-size:16px;font-weight:400;line-height:26px;color:var(--navy)}
.step p{position:absolute;left:104px;top:80px;width:180px;font-size:13px;line-height:22px;color:var(--muted)}

/* why */
.why{top:950px;left:0;width:1200px;height:480px;background:var(--band)}
.why-card{top:1120px;width:300px;height:248px;background:var(--white);border:1px solid var(--line)}
.why-card svg{position:absolute;left:114px;top:38px}
.why-card h3{position:absolute;top:138px;left:0;width:100%;text-align:center;font-size:18px;font-weight:400;color:var(--ink)}
.why-card hr{position:absolute;top:180px;left:0;width:100%;border:0;border-top:1px solid var(--line)}
.why-card p{position:absolute;top:194px;left:20px;width:220px;font-size:13px;line-height:22px;color:var(--muted)}
.why-card .link{position:absolute;right:22px;top:204px}
.side-arrow{top:1224px;width:36px;height:34px;background:#d8d8d8}

/* services */
.services{top:1430px;left:0;width:1200px;height:412px;background:var(--brand-soft)}
.service{width:240px;text-align:center;color:var(--white)}
.service h3{font-size:19px;font-weight:400;margin-top:18px}
.service p{font-size:13px;line-height:20px;margin-top:10px}
.service .more{display:inline-block;margin-top:12px;width:100px;height:36px;line-height:32px;border:2px solid var(--white);font-size:12px}
.service svg{display:block;margin:0 auto}

/* testimonials */
.voices{top:1842px;left:0;width:1200px;height:392px;background:linear-gradient(180deg,#3c4048 0%,#5a5f67 45%,#33373e 100%)}
.avatar{width:92px;height:92px;border-radius:50%;border:4px solid var(--white);background:#b8a99a}
.who{font-size:13px;color:var(--white);width:120px;text-align:center}
.bubble{top:2020px;width:328px;height:114px;background:var(--white);padding:18px 18px 0 26px;font-size:12.5px;line-height:20px;font-style:italic;color:var(--muted)}
.bubble::before{content:"";position:absolute;left:-12px;top:20px;border-top:10px solid transparent;border-bottom:10px solid transparent;border-right:12px solid var(--white)}
.bubble .read{position:absolute;right:28px;bottom:14px;font-style:normal;color:var(--red)}

/* follow */
.social{display:flex;gap:26px;justify-content:center;top:2354px}
.social span{display:flex;align-items:center;gap:8px;font-size:14px;color:var(--brand)}
.social i{width:40px;height:40px;border-radius:6px;background:var(--brand)}

/* cta */
.cta{top:2450px;left:0;width:1200px;height:304px;background:var(--cta)}
.cta-text{top:2510px;font-size:26px;line-height:44px;color:var(--white)}
.btn-bank{left:340px;top:2624px;width:242px;height:60px;background:var(--beige);text-align:center;color:var(--ink);font-size:16px;padding-top:10px}
.btn-bank small{display:block;font-size:11px;margin-top:4px}
.btn-biz{left:620px;top:2624px;width:242px;height:60px;line-height:60px;background:var(--teal);text-align:center;color:var(--white);font-size:16px}

/* partners */
.partners{top:2814px;left:0;width:1200px;display:flex;align-items:center;justify-content:center;gap:46px;font-size:24px;font-weight:700;color:var(--ink)}
.partners .arrow{font-weight:400;color:var(--muted);font-size:26px}

/* footer */
.site-footer{top:2906px;left:0;width:1200px;height:99px;background:var(--footer)}
.copy{left:132px;top:50px;font-size:12px;color:#bdbdbd}
.to-top{left:1022px;top:30px;width:38px;height:40px;background:#222;color:#ddd;font-size:9px;text-align:center;padding-top:20px}
</style>
</head>
<body>

<header class="site-header">
  <div class="abs brand-mark"></div>
  <div class="abs brand-name">VOLBEX</div>
  <div class="abs brand-tag">pathways for trade momentum</div>
  <nav class="nav">
    <a class="active" style="left:444px">Home</a>
    <a style="left:530px">About</a>
    <a style="left:590px">Portfolio</a>
    <a style="left:672px">Blog</a>
    <a style="left:722px">Feature</a>
    <a style="left:796px">Contacts</a>
  </nav>
  <div class="abs btn-register">Register Your Business</div>
</header>

<section class="abs hero" role="img" aria-label="Dusk skyline of a dense city with tall office towers"></section>
<div class="abs center hero-title">NEQUE PORRO</div>
<div class="abs center hero-sub">QUISQUAM EST QUI DOLOREM</div>
<div class="abs center hero-text">Lorem ipsum dolor sit amet, consectetur adipiscing elit, sed do eiusmod<br>tempor incididunt ut labore et dolore magna.</div>
<div class="abs center dots" style="top:438px"><span class="on"></span><span></span><span></span><span></span></div>

<h2 class="abs center" style="top:668px">How does <b>Volbex</b> work?</h2>
<div class="abs step" style="left:130px"><div class="step-num">01</div><h3>Tell us what you need done</h3><p>Answer a few questions about your job.</p></div>
<div class="abs step" style="left:450px"><div class="step-num">02</div><h3>Get competitive quotes</h3><p>Verified businesses send you quotes fast.</p></div>
<div class="abs step" style="left:770px"><div class="step-num">03</div><h3>Hire the best business</h3><p>Compare their quotes, profile and reviews.</p></div>

<section class="abs why"></section>
<h2 class="abs center" style="top:1008px">Why choose <b>Volbex</b></h2>
<div class="abs center" style="top:1060px;font-size:16px;color:var(--ink)">Over 40,000 businesses ready to quote on your work.</div>
<div class="abs side-arrow" style="left:0"><svg width="36" height="34"><path d="M20 11l-6 6 6 6" stroke="#fff" stroke-width="2" fill="none"/></svg></div>
<div class="abs side-arrow" style="left:1164px"><svg width="36" height="34"><path d="M16 11l6 6-6 6" stroke="#fff" stroke-width="2" fill="none"/></svg></div>

<div class="abs why-card" style="left:130px">
  <svg width="72" height="72" viewBox="0 0 72 72"><circle cx="34" cy="38" r="30" fill="none" stroke="#4f63a5" stroke-width="5"/><path d="M18 38l12 12 32-40" fill="none" stroke="#4f63a5" stroke-width="8" stroke-linecap="round"/></svg>
  <h3>Volbex Verified</h3><hr><p>Lorem ipsum dolor sit amet, conse ctetur adipiscing elit.</p>
  <svg class="link" width="18" height="18" viewBox="0 0 18 18"><path d="M7 11l4-4M5 9l-2 2a3 3 0 004 4l2-2M13 9l2-2a3 3 0 00-4-4L9 5" stroke="#ccc" stroke-width="1.5" fill="none"/></svg>
</div>
<div class="abs why-card" style="left:450px">
  <svg width="72" height="72" viewBox="0 0 72 72"><path d="M36 6L2 36h10v30h18V48h12v18h18V36h10z" fill="#4f63a5"/></svg>
  <h3>Home Care Guarantee</h3><hr><p>Lorem ipsum dolor sit amet, conse ctetur adipiscing elit.</p>
  <svg class="link" width="18" height="18" viewBox="0 0 18 18"><path d="M7 11l4-4M5 9l-2 2a3 3 0 004 4l2-2M13 9l2-2a3 3 0 00-4-4L9 5" stroke="#ccc" stroke-width="1.5" fill="none"/></svg>
</div>
<div class="abs why-card" style="left:770px">
  <svg width="72" height="72" viewBox="0 0 72 72"><circle cx="36" cy="36" r="30" fill="none" stroke="#4f63a5" stroke-width="5"/><path d="M36 16v20l12 10" fill="none" stroke="#4f63a5" stroke-width="5" stroke-linecap="round"/></svg>
  <h3>On-time Guarantee</h3><hr><p>Lorem ipsum dolor sit amet, conse ctetur adipiscing elit.</p>
  <svg class="link" width="18" height="18" viewBox="0 0 18 18"><path d="M7 11l4-4M5 9l-2 2a3 3 0 004 4l2-2M13 9l2-2a3 3 0 00-4-4L9 5" stroke="#ccc" stroke-width="1.5" fill="none"/></svg>
</div>

<section class="abs services"></section>
<div class="abs center" style="top:1476px;font-size:28px;color:var(--white)">Services Provides</div>
<div class="abs service" style="left:116px;top:1566px">
  <svg width="80" height="60" viewBox="0 0 80 60"><rect x="2" y="14" width="12" height="30" fill="#fff"/><rect x="66" y="14" width="12" height="30" fill="#fff"/><path d="M16 18h16l8 6 8-6h16v22l-18 12-12-10-18 0z" fill="#fff"/></svg>
  <h3>Legal Service</h3><p>penatibus et magnis dis parturient<br>montes nascetur ridiculus</p><span class="more">Learn More</span>
</div>
<div class="abs service" style="left:360px;top:1556px">
  <svg width="80" height="70" viewBox="0 0 80 70"><circle cx="40" cy="18" r="14" fill="#fff"/><path d="M8 70c0-22 14-30 32-30s32 8 32 30z" fill="#fff"/><path d="M36 40l4 20 4-20z" fill="#6680bb"/></svg>
  <h3>Accountant Service</h3><p>penatibus et magnis dis parturient<br>montes nascetur ridiculus</p><span class="more">Learn More</span>
</div>
<div class="abs service" style="left:598px;top:1556px">
  <svg width="80" height="70" viewBox="0 0 80 70"><circle cx="52" cy="12" r="10" fill="#fff"/><ellipse cx="40" cy="44" rx="28" ry="20" fill="#fff"/><rect x="22" y="56" width="8" height="12" fill="#fff"/><rect x="50" y="56" width="8" height="12" fill="#fff"/><rect x="8" y="38" width="8" height="8" fill="#fff"/></svg>
  <h3>Debt Funding</h3><p>penatibus et magnis dis parturient<br>montes nascetur ridiculus</p><span class="more">Learn More</span>
</div>
<div class="abs service" style="left:840px;top:1556px">
  <svg width="80" height="70" viewBox="0 0 80 70"><path d="M40 6a30 26 0 100 52l4 10 8-12A30 26 0 0040 6z" fill="#fff"/><text x="40" y="44" text-anchor="middle" font-family="Arimo,Arial,sans-serif" font-weight="700" font-size="34" fill="#6680bb">?</text></svg>
  <h3>Advices</h3><p>penatibus et magnis dis parturient<br>montes nascetur ridiculus</p><span class="more">Learn More</span>
</div>

<section class="abs voices" role="img" aria-label="Blurred silhouettes of business people standing in an office"></section>
<div class="abs center" style="top:1896px;font-size:28px;color:var(--white)">What our customers have to say.</div>
<div class="abs center" style="top:1946px;font-size:16px;font-weight:700;color:var(--white)">Don't just take our word for it. Real people. Real experiences.</div>
<div class="abs avatar" style="left:124px;top:2014px" role="img" aria-label="Portrait of customer Marlon"></div>
<div class="abs who" style="left:110px;top:2124px">Marlon</div>
<div class="abs bubble" style="left:246px">“ Neque porro quisquam est qui dolorem ipsum quia dolor sit amet, consectetur, adipisci velit. Neque porro quisquam. ”<span class="read">Read More &gt;&gt;</span></div>
<div class="abs avatar" style="left:626px;top:2020px;background:#c7a58a" role="img" aria-label="Portrait of customer Tobias"></div>
<div class="abs who" style="left:612px;top:2126px">Tobias</div>
<div class="abs bubble" style="left:750px">“ Neque porro quisquam est qui dolorem ipsum quia dolor sit amet, consectetur, adipisci velit. Neque porro quisquam. ”<span class="read">Read More &gt;&gt;</span></div>
<div class="abs center dots" style="top:2174px"><span class="on" style="background:#fff;border-color:#fff"></span><span></span><span></span><span></span></div>

<div class="abs center" style="top:2298px;font-size:28px;color:var(--ink)">Follow us for our latest offers and handy lifestyle tips!</div>
<div class="abs center social">
  <span><i></i>Circlepage</span>
  <span><i></i>Chirpline</span>
  <span><i></i>Peerlane</span>
</div>

<section class="abs cta"></section>
<div class="abs center cta-text">Every day thousands of customers come to Volbex to find the best<br>businesses in their area. Why not give it a go?</div>
<div class="abs btn-bank">Reigster for Banking<small>Legal and Accounting Freelancers</small></div>
<div class="abs btn-biz">Register Your Business</div>

<div class="abs partners">
  <span class="arrow">‹</span>
  <span>Quarrin</span><span>Belvane</span><span>Tessaro</span><span>Rivola</span><span>Moss</span><span>Kestrel</span>
  <span class="arrow">›</span>
</div>

<footer class="abs site-footer">
  <div class="abs copy">Copyright ©2014. Yoursite. All Right Reserved.</div>
  <div class="abs to-top">TOP</div>
</footer>

</body>
</html>
```